Alternative Health Practice - Website redesign

With regard to the welcome image, stock photos can't show the faces of other people. And please don't submit a design for a one-page website.
Hello, I am redesigning a website and need some help from a professional.
The old website is here: peter-lindqvist.net (pls note I don't want to reuse the welcome photo from the old site). Much of the written content will remain the same, so note that I also need a page layout/text colour etc that works for text heavy pages: ie www.peter-lindqvist.net/somatic-articles and www.peter-lindqvist.net/client-reviews
My effort at redesigning is underway here: https://pjlindqvist.sitebuildr.net/my-site-7
The original sitebuildr template is this one: https://www.sitebuildr.net/website-template/view/html/2868?originUrl=https%3A%2F%2Fwww.sitebuildr.net%2Fwebsite%2Ftemplates%2Fhtml%2Fhealth-wellness&tpClick=view_button&esi=6305f015-f1b5-4bdd-8dfa-47b7d756bb68
I'm pretty happy with the colour palette. My name Peter Johan Lindqvist is now the "brand" without Rooted Stillness subtitle. Regarding the Welcome section, if you are going to use my photos, it probably needs to be those two that are already there. If you want to put a stock photo there instead, that's fine.
If you want to propose something quite different to my design, I'm happy to receive design files in Photoshop or whatever and then subsequently replicate on Sitebuildr. Up to you.
Target Market(s)
Mostly women, some men ages 28-60.
Coding
Coded - Design and coding required
Number of Pages Required
5+ page
Look and feel
Each slider illustrates characteristics of the customer's brand and the style your logo design should communicate.

```html
<!DOCTYPE html>
<html lang="en">
<head>
<meta charset="utf-8">
<title>Peter Lindqvist – Energy Healing</title>
<link href="https://fonts.googleapis.com/css2?family=Open+Sans:wght@400;600;700;800&display=swap" rel="stylesheet">
<style>
:root{
  --gold:#b4893a;
  --gold-dark:#8c6422;
  --gold-light:#d2a85a;
  --ink:#1f1f1f;
  --text:#3a3a3a;
  --white:#ffffff;
  --footer:#262626;
  --card-border:#e6e6e6;
}
*{box-sizing:border-box;margin:0;padding:0}
html,body{width:1200px;height:3432px;overflow:hidden}
body{position:relative;font-family:"Open Sans",Arial,sans-serif;color:var(--text);background:var(--white)}
.abs{position:absolute}
.btn{position:absolute;display:flex;align-items:center;justify-content:center;background:linear-gradient(90deg,var(--gold-dark),var(--gold-light) 55%,var(--gold));color:var(--white);font-weight:700;font-size:15px;letter-spacing:1px;border-radius:3px}

/* header */
.site-header{position:absolute;left:0;top:0;width:1200px;height:74px;display:flex;align-items:center;justify-content:space-between;padding:0 40px 0 100px;z-index:3;background:rgba(20,16,12,.45)}
.brand{display:flex;align-items:center;gap:10px;color:var(--gold-light);font-weight:700;font-size:17px;letter-spacing:1px}
.brand-dot{width:30px;height:30px;border-radius:50%;background:var(--gold)}
.main-nav{display:flex;gap:28px;align-items:center;color:var(--white);font-size:14px;font-weight:600;letter-spacing:.5px}
.lang-flag{width:22px;height:14px;background:var(--gold-light);border-radius:2px}

/* hero */
.hero{position:absolute;left:0;top:0;width:1200px;height:862px;background:linear-gradient(160deg,#6e5a4a 0%,#a38a77 30%,#3f3540 60%,#5a4a5c 80%,#2a2420 100%)}
.hero-shade{position:absolute;inset:0;background:rgba(20,14,10,.35)}
.hero h1{position:absolute;left:0;width:1200px;top:378px;text-align:center;color:var(--white);font-size:58px;font-weight:800;letter-spacing:2px}
.hero p{position:absolute;left:0;width:1200px;top:478px;text-align:center;color:var(--white);font-size:22px}

/* intro sections */
.photo{position:absolute;border-radius:22px;overflow:hidden}
.section-title{position:absolute;color:var(--ink);font-weight:800;font-size:34px;letter-spacing:1px}
.section-text{position:absolute;font-size:16px;line-height:1.4;color:var(--text)}
.portrait{position:absolute;border-radius:50%;border:6px solid var(--white);background:linear-gradient(135deg,#c7a58a,#7a6a55)}

/* experience */
.experience-title{position:absolute;left:0;width:1200px;top:2192px;text-align:center;color:var(--ink);font-weight:800;font-size:34px}
.experience-sub{position:absolute;left:0;width:1200px;top:2246px;text-align:center;font-size:16px}
.card{position:absolute;top:2292px;width:260px;height:290px;border:1px solid var(--card-border);border-radius:8px;background:var(--white);box-shadow:0 3px 10px rgba(0,0,0,.08);padding:22px 20px}
.card p{font-size:14px;line-height:1.35;color:var(--text)}
.card .avatar{position:absolute;left:22px;top:196px;width:72px;height:72px;border-radius:50%;background:linear-gradient(135deg,#b08d74,#5b4a3c)}
.card .name{position:absolute;left:108px;top:210px;color:var(--gold);font-weight:700;font-size:14px;line-height:1.3}

/* footer */
.site-footer{position:absolute;left:0;top:2770px;width:1200px;height:662px;background:linear-gradient(135deg,#333 0%,#222 50%,#2c2c2c 100%)}
.contact-title{position:absolute;left:172px;top:150px;color:var(--white);font-weight:800;font-size:36px}
.contact-line{position:absolute;left:172px;display:flex;gap:14px;color:var(--white);font-size:15px;line-height:1.35}
.contact-line svg{flex:none}
.social{position:absolute;left:172px;top:490px;display:flex;gap:14px}
.social span{width:26px;height:26px;border-radius:50%;border:2px solid var(--white)}
.contact-form{position:absolute;left:600px;top:90px;width:486px;height:482px;border:2px solid #8a8a8a;border-radius:18px;background:rgns(0,0,0,0);background:rgba(0,0,0,.25)}
.field{position:absolute;color:var(--white);font-weight:700;font-size:14px;letter-spacing:.5px;border-bottom:1px solid #bbb;padding-bottom:26px}
</style>
</head>
<body>

<section class="hero" role="img" aria-label="Hands resting on a client during an energy healing session">
  <div class="hero-shade"></div>
  <h1>ENERGY HEALING</h1>
  <p>Balance, Purpose, Success, Creativity, Clarity, Ease, Discovery, Presence, Harmony, Joy</p>
  <div class="btn" style="left:508px;top:528px;width:184px;height:42px">BOOK A SESSION</div>
</section>

<header class="site-header">
  <div class="brand"><span class="brand-dot"></span>PETER LINDQVIST</div>
  <nav class="main-nav">
    <span>THE PRACTICE</span><span>ABOUT ME</span><span>FEEDBACK</span><span>APPROACH</span><span>CONTACT</span><span class="lang-flag"></span>
  </nav>
</header>

<div class="photo" style="left:82px;top:944px;width:484px;height:526px;background:linear-gradient(160deg,#e9e4de,#cbbfb2 45%,#8a7868)" role="img" aria-label="Practitioner's hands cradling a client's head on a treatment table"></div>
<h2 class="section-title" style="left:668px;top:1072px">ENERGY HEALING</h2>
<p class="section-text" style="left:668px;top:1124px;width:300px">An session begins by identifying your intention or wish. You may be facing physical or emotional challenges or seeking healing with another aspect of your life...</p>
<div class="btn" style="left:668px;top:1232px;width:184px;height:46px">READ MORE</div>

<div class="photo" style="left:620px;top:1546px;width:486px;height:530px;background:linear-gradient(160deg,#9b8f86,#c9b49e 40%,#5d4d63 75%,#3f3548)" role="img" aria-label="Hands resting on a client draped in a patterned blanket"></div>
<div class="portrait" style="left:572px;top:1852px;width:210px;height:210px" role="img" aria-label="Portrait of the practitioner"></div>
<h2 class="section-title" style="left:124px;top:1728px">ABOUT ME</h2>
<p class="section-text" style="left:124px;top:1780px;width:310px">Growing up in Scotland I always had a strong connection with nature and the outdoors. Playing outside with friends, with trees...</p>
<div class="btn" style="left:124px;top:1870px;width:184px;height:46px">READ MORE</div>

<h2 class="experience-title">EXPERIENCE</h2>
<p class="experience-sub">Below is feedback sent direct to me from people who have come to the practice.</p>

<article class="card" style="left:62px"><p>You have given me a lot of confidence in myself. You are showing me a new way of life. And I've learned that it is possible to handle the physical pain caused by our emotions. I didn't know how to cope with it. Thank you...</p><div class="avatar" role="img" aria-label="Client photo"></div><div class="name">Lucía Moreno<br>Vidal</div></article>
<article class="card" style="left:336px"><p>You have given me a lot of confidence in myself. You are showing me a new way of life. And I've learned that it is possible to handle the physical pain caused by our emotions. I didn't know how to cope with it. Thank you...</p><div class="avatar" role="img" aria-label="Client photo"></div><div class="name">Lucía Moreno<br>Vidal</div></article>
<article class="card" style="left:610px"><p>You have given me a lot of confidence in myself. You are showing me a new way of life. And I've learned that it is possible to handle the physical pain caused by our emotions. I didn't know how to cope with it. Thank you...</p><div class="avatar" role="img" aria-label="Client photo"></div><div class="name">Lucía Moreno<br>Vidal</div></article>
<article class="card" style="left:884px"><p>You have given me a lot of confidence in myself. You are showing me a new way of life. And I've learned that it is possible to handle the physical pain caused by our emotions. I didn't know how to cope with it. Thank you...</p><div class="avatar" role="img" aria-label="Client photo"></div><div class="name">Lucía Moreno<br>Vidal</div></article>

<div class="btn" style="left:508px;top:2620px;width:184px;height:46px">READ MORE</div>

<footer class="site-footer">
  <h2 class="contact-title">CONTACT US</h2>
  <div class="contact-line" style="top:220px">
    <svg width="18" height="22" viewBox="0 0 18 22"><path d="M9 1a7 7 0 0 0-7 7c0 5 7 13 7 13s7-8 7-13a7 7 0 0 0-7-7z" fill="none" stroke="#fff" stroke-width="1.6"/><circle cx="9" cy="8" r="2.5" fill="none" stroke="#fff" stroke-width="1.6"/></svg>
    <span>Rua das Flores 12b<br>Bairro Alto<br>Lisbon, Portugal, 1200-195</span>
  </div>
  <div class="contact-line" style="top:310px">
    <svg width="18" height="18" viewBox="0 0 18 18"><path d="M4 1l3 4-2 2a10 10 0 0 0 6 6l2-2 4 3-2 3C8 17 1 10 1 3z" fill="none" stroke="#fff" stroke-width="1.5" stroke-linejoin="round"/></svg>
    <span>Telephone/Whatsapp: (+351) 91 204 7731</span>
  </div>
  <div class="contact-line" style="top:362px">
    <svg width="20" height="16" viewBox="0 0 20 16"><rect x="1" y="1" width="18" height="14" rx="1.5" fill="none" stroke="#fff" stroke-width="1.5"/><path d="M1 2l9 7 9-7" fill="none" stroke="#fff" stroke-width="1.5"/></svg>
    <span>Email: info@peter-lindqvist.net</span>
  </div>
  <div class="social"><span></span><span></span></div>

  <form class="contact-form">
    <div class="field" style="left:32px;top:30px;width:420px">NAME</div>
    <div class="field" style="left:32px;top:110px;width:196px">EMAIL</div>
    <div class="field" style="left:256px;top:110px;width:196px">PHONE</div>
    <div class="field" style="left:32px;top:190px;width:420px;padding-bottom:80px">MESSAGE</div>
    <div class="btn" style="left:32px;top:390px;width:184px;height:42px">SUBMIT</div>
  </form>
</footer>

</body>
</html>
```